Boho Flower and Curiosities Shop Needs a Non-tradtional Calendar of Events

Hi! I own a cute flower shop called Meadowlark Petals. I have lots of things going on at the shop and I'd love a calendar of events poster to put around town. I already have dates and times and descriptions. I have a very boho aesthetic, creative, whimsical and different. I'd like this calendar of events to be not cookie cutter. Something interesting with images and interesting font that matches my logo. Not a super busy design.

My events can be found here: https://www.meadowlarkpetals.example/calendar-of-events

I want to be able to easily edit the poster so I can use it in the future.

Target Market(s)

Locals who want an alternative something to do.

Industry/Entity Type

Shop

Colors

Designer to choose colors to be used in the design.

Requirements
Must have
• must have the same kind of vibe that my logo and especially the mural on my building has (I submitted an image of the building). Unique, not cheesy.
• Must be editable so I can use it in the future.
Nice to have
• I want it to have a call to action such as visit my website "www.meadowlarkpetals.example". Also I like the idea of calling it Shop Happenings instead of Events Calendar.
• It might be cool to have the events coming off of a dream catcher like (but not exactly in fact I think it can be more whimsical and perhaps my logo in the middle of the catcher) the one attached.
Should not have
• If you do include flowers - no roses or daisies! Please.

```html
<!DOCTYPE html>
<html lang="en">
<head>
<meta charset="utf-8">
<title>Meadowlark Petals – Shop Happenings</title>
<link rel="stylesheet" href="https://fonts.googleapis.com/css2?family=Parisienne&family=Crimson+Text:ital,wght@0,400;0,700;1,400&display=swap">
<style>
  :root{
    --backdrop:#5f7560;
    --paper:#fbdcf3;
    --card:#ffffff;
    --ink:#141414;
    --ring:#b9a9b5;
    --frame:#e9905a;
    --oyster-a:#8a7d6c; --oyster-b:#c9bfae;
    --moss-a:#4f6b2e; --moss-b:#9c8f78;
    --kids-a:#8e2a2a; --kids-b:#e4d2c4;
    --bloom-a:#b2205f; --bloom-b:#f2b9cf;
    --table-a:#e9e4da; --table-b:#9aa07c;
    --fairy-a:#5aa53a; --fairy-b:#3e3528;
    --herb-a:#3f5a2c; --herb-b:#d9c8b8;
    --camomile-a:#4d5b36; --camomile-b:#e6e4d6;
    --wreath-a:#f7e6ee; --wreath-b:#f3c7d3;
    --corner-a:#f0602e; --corner-b:#f6c2a6;
  }
  *{box-sizing:border-box;margin:0;padding:0}
  html,body{width:1200px;height:1200px;overflow:hidden;background:var(--backdrop)}
  .poster{position:absolute;left:185px;top:16px;width:830px;height:1168px;background:var(--paper);overflow:hidden;color:var(--ink);font-family:"Crimson Text",Georgia,serif}
  .brand{position:absolute;left:298px;top:48px;width:210px;height:210px;border-radius:50%;background:radial-gradient(circle,var(--wreath-a) 55%,var(--wreath-b));display:flex;align-items:center;justify-content:center;text-align:center}
  .brand-name{font-family:"Parisienne",cursive;font-weight:400;font-size:40px;line-height:1.05;color:var(--ink)}
  .event{position:absolute;width:370px;height:200px;z-index:2}
  .event-photo{position:absolute;left:0;top:0;width:255px;height:161px}
  .event-card{position:absolute;left:159px;top:-17px;width:192px;height:192px;border-radius:50%;background:var(--card);border:1px solid var(--ring);text-align:center;padding:20px 12px 0;display:flex;flex-direction:column;align-items:center}
  .event-title{font-family:"Parisienne",cursive;font-weight:400;font-size:18px;line-height:1.15;height:46px;display:flex;align-items:center;justify-content:center;width:150px}
  .event-title--long{font-size:16px;height:54px;line-height:1.1;margin-top:-4px}
  .event-date{font-weight:700;font-size:15px;margin-top:6px;line-height:1.15}
  .event-info{font-size:11.5px;line-height:1.3}
  .event-card--tbd .event-date{font-size:14px;margin-top:4px;line-height:1.1}
  .event-card--tbd .event-info{margin-top:3px}
  .col-left{left:34px}
  .col-right{left:441px}
  .corner-flowers{position:absolute;left:740px;top:955px;width:90px;height:130px;z-index:1;border-radius:50% 0 0 50%;background:radial-gradient(circle at 60% 50%,var(--corner-a),var(--corner-b) 60%,transparent 72%)}
  .cta{position:absolute;left:183px;top:1057px;width:463px;height:62px;background:var(--card);border:1.5px solid var(--frame);display:flex;align-items:center;justify-content:center;font-style:italic;font-size:30px}
</style>
</head>
<body>
<main class="poster">
  <header class="brand"><h1 class="brand-name">Meadowlark<br>Petals</h1></header>

  <article class="event col-left" style="top:246px">
    <div class="event-photo" role="img" aria-label="Pile of fresh oysters" style="background:linear-gradient(135deg,var(--oyster-a),var(--oyster-b))"></div>
    <div class="event-card">
      <h2 class="event-title">Tidewater Oyster Co. Roast!</h2>
      <p class="event-date">Jan 21, 2018</p>
      <p class="event-info">at 2:00pm - 5:00pm EST<br>Meadowlark Petals,<br>318 Fernbrook Ave,<br>Harlow Bay,<br>SC 29901, USA</p>
    </div>
  </article>

  <article class="event col-right" style="top:246px">
    <div class="event-photo" role="img" aria-label="Glass terrarium with moss" style="background:linear-gradient(135deg,var(--moss-b),var(--moss-a))"></div>
    <div class="event-card">
      <h2 class="event-title">Terrariums &amp; Tapas</h2>
      <p class="event-date">Jan 31, 2018</p>
      <p class="event-info">at 5:30pm - 7:00pm EST<br>Meadowlark Petals, 318<br>Fernbrook Ave, Harlow<br>Bay,<br>SC 29901, USA</p>
    </div>
  </article>

  <article class="event col-left" style="top:446px">
    <div class="event-photo" role="img" aria-label="Two children wearing flower crowns" style="background:linear-gradient(135deg,var(--kids-a),var(--kids-b))"></div>
    <div class="event-card">
      <h2 class="event-title">Mother Daughter Flower Crown Making</h2>
      <p class="event-date">Feb 10, 2018</p>
      <p class="event-info">at 10:30am - 12:00pm EST<br>Meadowlark Petals,<br>318 Fernbrook Ave,<br>Harlow Bay,<br>SC 29901, USA</p>
    </div>
  </article>

  <article class="event col-right" style="top:446px">
    <div class="event-photo" role="img" aria-label="Pink and white flower arrangement" style="background:linear-gradient(135deg,var(--bloom-b),var(--bloom-a))"></div>
    <div class="event-card">
      <h2 class="event-title">Valentines Day Flower Arranging</h2>
      <p class="event-date">Feb 13, 2018</p>
      <p class="event-info">at 5:30pm - 7:00pm EST<br>Meadowlark Petals, 318<br>Fernbrook Ave, Harlow<br>Bay,<br>SC 29901, USA</p>
    </div>
  </article>

  <article class="event col-left" style="top:645px">
    <div class="event-photo" role="img" aria-label="Dinner table set with glasses and flowers" style="background:linear-gradient(135deg,var(--table-b),var(--table-a))"></div>
    <div class="event-card">
      <h2 class="event-title">Valentines Pop-up Dinner</h2>
      <p class="event-date">Feb 14, 2018</p>
      <p class="event-info">at 6:00pm - 8:00pm<br>EST Meadowlark Petals,<br>318 Fernbrook Ave,<br>Harlow Bay,<br>SC 29901, USA</p>
    </div>
  </article>

  <article class="event col-right" style="top:645px">
    <div class="event-photo" role="img" aria-label="Fairy garden terrarium with moss and stones" style="background:linear-gradient(180deg,var(--fairy-a),var(--fairy-b))"></div>
    <div class="event-card">
      <h2 class="event-title">Fairy Garden Terrariums</h2>
      <p class="event-date">Mar 3, 2018</p>
      <p class="event-info">at 10:30am - 12:00pm<br>EST Meadowlark Petals,<br>318 Fernbrook Ave,<br>Harlow Bay,<br>SC 29901, USA</p>
    </div>
  </article>

  <article class="event col-left" style="top:846px">
    <div class="event-photo" role="img" aria-label="Botanical illustration of a mandrake plant" style="background:linear-gradient(135deg,var(--herb-b),var(--herb-a))"></div>
    <div class="event-card">
      <h2 class="event-title">Mandrake Print Making</h2>
      <p class="event-date">Mar 14, 2018</p>
      <p class="event-info">at 5:30pm - 7:00pm<br>EDT Meadowlark Petals,<br>318 Fernbrook Ave,<br>Harlow Bay,<br>SC 29901, USA</p>
    </div>
  </article>

  <article class="event col-right" style="top:846px">
    <div class="event-photo" role="img" aria-label="Chamomile flowers growing in a field" style="background:linear-gradient(135deg,var(--camomile-a),var(--camomile-b))"></div>
    <div class="event-card event-card--tbd">
      <h2 class="event-title event-title--long">Medicinal Flowers, Herb and Gardening Series</h2>
      <p class="event-date">Time TBD -<br>Coming Soon</p>
      <p class="event-info">Meadowlark Petals,<br>318 Fernbrook Ave,<br>Harlow Bay,<br>SC 29901, USA</p>
    </div>
  </article>

  <div class="corner-flowers" role="img" aria-label="Watercolour cluster of orange blossoms"></div>

  <footer class="cta">www.meadowlarkpetals.example</footer>
</main>
</body>
</html>
```